Design Only - Custom Travel Brand E-Commerce *

I have a basic website layout already made on Shopify, but looking for some additional design touches on a few pages. We would like to add some more style and creativity to the site. The images on the site are not final, just placeholders.

We are a travel brand selling our first 2 items (custom luggage tag & passport wallet). The premise is to engrave the product with everywhere you have been and everywhere you will go. You are allowed to ship back to us and re-engrave new places for $5.

The customizer page is already coded but we can make changes to the forms (select countries, enter contact information form, and overall flow)

Target Market(s)

Millennials and travelers. Most likely more females then males will be purchasing. Also for parents buying children gift cards/gifts

Industry/Entity Type

E-Commerce

Number of Pages Required

5+ page

Font styles to use
Sans Serif

Colors
85cae6
3176b5
acd136

Requirements
Must have
• Looking for ways to add some new design to the pages. It's a new product category so want the customer to fully understand what it is and how it works. The gifting page will be important because you can either buy a blank tag/passport holder as a gift ($5 paid one-time return included) or a gift card from the gifting page.
Nice to have
• Looking to add a bit of color. Gray is ok. Brand is primarily black and white but would be nice to add a TINY pop of color on certain buttons maybe.
Should not have
• The customizer feature is fixed. You can change the form look/feel.

```html
<!DOCTYPE html>
<html lang="en">
<head>
<meta charset="utf-8">
<title>Wandermark — Gifting</title>
<link rel="stylesheet" href="https://fonts.googleapis.com/css2?family=Nunito+Sans:wght@400;600;700&family=Oswald:wght@300;600&display=swap">
<style>
  :root {
    --lime: #acd136;
    --blue: #3176b5;
    --sky: #85cae6;
    --ink: #111111;
    --text: #333333;
    --muted: #4a4a4a;
    --button: #555555;
    --footer: #f4f4f4;
    --rule: #e2e2e2;
    --white: #ffffff;
  }
  * { box-sizing: border-box; margin: 0; padding: 0; }
  html, body { width: 833px; height: 1200px; overflow: hidden; background: var(--white); }
  body { position: relative; font-family: "Nunito Sans", Arial, sans-serif; color: var(--text); }
  .abs { position: absolute; }

  .promo-bar { left: 0; top: 0; width: 833px; height: 27px; background: var(--lime); display: flex; align-items: center; justify-content: center; gap: 8px; color: var(--white); font-size: 8px; font-weight: 600; }
  .site-header { left: 0; top: 27px; width: 833px; height: 40px; border-bottom: 1px solid var(--rule); }
  .brand { left: 77px; top: 8px; height: 24px; display: flex; align-items: center; gap: 5px; font-family: "Oswald", sans-serif; font-weight: 600; font-size: 14px; letter-spacing: 1.5px; color: var(--ink); }
  .brand-square { width: 7px; height: 7px; background: var(--ink); }
  .main-nav { left: 0; width: 833px; top: 12px; display: flex; justify-content: center; gap: 18px; font-size: 10px; color: var(--ink); }
  .main-nav .current { color: var(--blue); }
  .header-icons { left: 686px; top: 11px; display: flex; gap: 11px; }

  .page-title { left: 0; top: 90px; width: 833px; text-align: center; font-family: "Oswald", sans-serif; font-size: 31px; color: var(--ink); line-height: 40px; }
  .page-title strong { font-weight: 600; }
  .page-title span { font-weight: 300; }
  .page-subtitle { left: 0; top: 151px; width: 833px; text-align: center; font-size: 14.5px; font-weight: 600; letter-spacing: 0.2px; color: var(--text); }

  .hero { left: 77px; top: 181px; width: 679px; height: 355px; background: linear-gradient(90deg, #a7d2de 0%, #b9dde5 45%, #8fc8db 70%, #2f47a6 100%); }
  .hero-copy { left: 112px; top: 321px; width: 340px; font-family: "Oswald", sans-serif; font-weight: 600; font-size: 22px; line-height: 31px; color: var(--white); letter-spacing: -0.3px; }

  .section-title { left: 0; top: 584px; width: 833px; text-align: center; font-family: "Oswald", sans-serif; font-size: 31px; color: var(--ink); line-height: 40px; }
  .section-title strong { font-weight: 600; }
  .section-title span { font-weight: 300; }

  .gift-option { top: 643px; width: 297px; text-align: center; }
  .gift-option .photo { width: 297px; height: 197px; }
  .gift-option h3 { margin-top: 16px; font-size: 11px; font-weight: 700; letter-spacing: 0.3px; color: var(--ink); }
  .gift-option p { margin-top: 8px; font-size: 9.5px; line-height: 19.5px; color: var(--muted); }
  .gift-option .btn { display: inline-block; margin-top: 9px; height: 32px; line-height: 32px; padding: 0 11px; background: var(--button); color: var(--white); font-size: 9.5px; font-weight: 700; letter-spacing: 0.2px; }
  .option-blank { left: 104px; }
  .option-blank .photo { background: linear-gradient(135deg, #6b6b6b, #4a4a4a 60%, #5c5c5c); }
  .option-card { left: 432px; }
  .option-card .photo { background: linear-gradient(90deg, #8a5a50 0%, #b28078 30%, #6fc2e6 55%, #8bcbe8 75%, #6c6f86 100%); }

  .site-footer { left: 0; top: 1023px; width: 833px; height: 120px; background: var(--footer); border-bottom: 1px solid var(--rule); }
  .footer-heading { font-size: 10.5px; font-weight: 700; color: var(--ink); }
  .quick-links-title { left: 77px; top: 1072px; }
  .quick-links { left: 77px; top: 1097px; display: flex; gap: 14px; font-size: 9.5px; color: var(--ink); }
  .newsletter-title { left: 491px; top: 1070px; }
  .newsletter-form { left: 488px; top: 1091px; width: 267px; height: 33px; display: flex; }
  .newsletter-form .field { flex: 1; background: var(--white); border: 1px solid #cfcfcf; border-right: 0; padding-left: 15px; line-height: 31px; font-size: 9px; color: var(--text); }
  .newsletter-form .submit { width: 85px; background: var(--blue); color: var(--white); font-size: 10px; font-weight: 700; text-align: center; line-height: 33px; }

  .payments { left: 77px; top: 1161px; display: flex; gap: 4px; align-items: center; }
  .pay-card { width: 36px; height: 23px; border-radius: 2px; }
  .socials { left: 615px; top: 1154px; display: flex; gap: 14px; }
  .social { width: 11px; height: 11px; background: var(--ink); border-radius: 2px; }
  .copyright { left: 555px; top: 1177px; width: 200px; text-align: right; font-size: 8.5px; color: var(--muted); }
</style>
</head>
<body>

  <div class="abs promo-bar">
    <svg width="18" height="11" viewBox="0 0 18 11" fill="none" stroke="#ffffff" stroke-width="1"><rect x="0.5" y="0.5" width="11" height="7"/><path d="M11.5 3h3.5l2.5 2.5v2.5h-6"/><circle cx="4" cy="9" r="1.3"/><circle cx="14" cy="9" r="1.3"/></svg>
    Free shipping on all orders over $35
  </div>

  <header class="abs site-header">
    <div class="abs brand"><span class="brand-square"></span>WANDERMARK</div>
    <nav class="abs main-nav">
      <span>Home</span><span>Shop</span><span class="current">Gifting</span><span>About Us</span><span>Register Your Tag</span>
    </nav>
    <div class="abs header-icons">
      <svg width="14" height="16" viewBox="0 0 14 16" fill="none" stroke="#111" stroke-width="1.2"><circle cx="7" cy="4.5" r="3.5"/><rect x="1" y="9" width="12" height="6" rx="3"/></svg>
      <svg width="15" height="16" viewBox="0 0 15 16" fill="none" stroke="#111" stroke-width="1.3"><circle cx="6.5" cy="6.5" r="5.5"/><path d="M10.5 10.5l4 4.5"/></svg>
      <svg width="15" height="16" viewBox="0 0 15 16" fill="none" stroke="#111" stroke-width="1.2"><rect x="1" y="4.5" width="13" height="11"/><path d="M4.5 6V3.5a3 3 0 0 1 6 0V6"/></svg>
    </div>
  </header>

  <h1 class="abs page-title"><strong>THE PREFECT GIFT</strong> <span>FOR ANY TRAVLER</span></h1>
  <p class="abs page-subtitle">CUSTOM TRAVEL BRAND REIMAGINED FOR MODERN LIFE</p>

  <div class="abs hero" role="img" aria-label="Wrapped blue gifts with ribbon, a toy airliner and passports on a pale blue surface"></div>
  <p class="abs hero-copy">LOREM IPSUMET, CONSECTETUR ADIPISCING ELIT, SED DO EIUSMOD</p>

  <h2 class="abs section-title"><strong>2 WAYS</strong> <span>TO GIFT</span></h2>

  <article class="abs gift-option option-blank">
    <div class="photo" role="img" aria-label="Black passport wallet and luggage tag in an open gift box"></div>
    <h3>PURCHASE A BLANK PRODUCT OR JUST INLTIALS</h3>
    <p>Choose to send a blank product or customise with their initials<br>*includes $5 one time returns shipping free</p>
    <span class="btn">BUY NOW</span>
  </article>

  <article class="abs gift-option option-card">
    <div class="photo" role="img" aria-label="Hand holding a phone showing a gift voucher"></div>
    <h3>SEND AN ONLINE CARD</h3>
    <p>Choose from one of our creative e-gift card and let them choose<br>the product they want.</p>
    <span class="btn">BUY GIFT CARD</span>
  </article>

  <footer class="abs site-footer"></footer>
  <h4 class="abs footer-heading quick-links-title">Quick links</h4>
  <nav class="abs quick-links">
    <span>Search</span><span>Shipping and Return Policy</span><span>Terms of Services</span><span>Contact</span>
  </nav>
  <h4 class="abs footer-heading newsletter-title">Newsletter</h4>
  <div class="abs newsletter-form">
    <div class="field">Email Address</div>
    <div class="submit">SUBSCRIBE</div>
  </div>

  <div class="abs payments" aria-label="Accepted payment methods">
    <span class="pay-card" style="background:#e6e6e6"></span>
    <span class="pay-card" style="background:#3f74b8"></span>
    <span class="pay-card" style="background:#5b9bd5"></span>
    <span class="pay-card" style="background:#e8e8e8"></span>
    <span class="pay-card" style="background:#d5d5d5;width:28px"></span>
    <span class="pay-card" style="background:#3aa641;width:18px;border-radius:50%"></span>
    <span class="pay-card" style="background:#ffffff;border:1px solid #888"></span>
  </div>

  <div class="abs socials" aria-label="Social links">
    <span class="social"></span><span class="social"></span><span class="social"></span><span class="social"></span>
  </div>
  <p class="abs copyright">© 2020 Wandermark. All Rights Reserved</p>

</body>
</html>
```